Business Card Design Project

Basketball Training program

Offers: Travel Club Program - Camps - Clinics - Private Training

website: ridgeportcourt.net
Phone Contact: Main Phone: 555-314-7720
Email: ridgeport.court@mailzone.example

Industry/Entity Type

Business

Contact Information for Business Card

Need one for the following coaches:
Marcus Thorne - Boys & Girls Basketball Coach
Kirasol Vendry - Girls Basketball Coach
Anselmo Trujar - Director/Head Coach
Walter Fisk- Boys Basketball
Howard Lindqvist - Boys Basketball
Ramon Etxeberri - Boys Basketball
Talvin Okafor- Boys Basketball/ Trainer
Al Hargrove - Boys & Girls Basketball Coach

Basketball Training program Logo - one side

Logo on the corner
new one on the left (RC)
old one on the right (old one is with the ridgeport and court)

```html
<!DOCTYPE html>
<html lang="en">
<head>
<meta charset="utf-8">
<title>Ridgeport Court – Business Cards</title>
<link rel="stylesheet" href="https://fonts.googleapis.com/css2?family=Source+Sans+3:ital,wght@0,400;0,600;0,700;1,400&display=swap">
<style>
  :root {
    --stage: #3a3a3a;
    --paper: #ffffff;
    --ink: #1c1c1c;
    --muted: #555555;
    --gold: #f6b10f;
    --night: #000000;
  }
  * { margin: 0; padding: 0; box-sizing: border-box; }
  html, body {
    width: 1200px; height: 750px; overflow: hidden;
    background: var(--stage);
    font-family: "Source Sans 3", sans-serif;
  }
  .stage { position: relative; width: 1200px; height: 750px; }
  .card {
    position: absolute; top: 221px;
    width: 540px; height: 308px;
  }
  .card--front { left: 40px; background: var(--paper); }
  .card--back { left: 620px; background: var(--night); }

  .monogram {
    position: absolute; left: 82px; top: 64px;
    width: 100px; height: 90px;
    display: flex; align-items: center; justify-content: center; gap: 8px;
  }
  .monogram__dot { width: 14px; height: 14px; border-radius: 50%; background: var(--ink); }
  .monogram__text { font-size: 44px; font-weight: 700; color: var(--ink); letter-spacing: 1px; }

  .wordmark {
    position: absolute; left: 62px; top: 178px; width: 140px;
    text-align: center; font-size: 22px; font-weight: 700; line-height: 1.05;
    color: var(--gold); text-transform: uppercase;
  }

  .divider {
    position: absolute; left: 232px; top: 62px;
    width: 2px; height: 200px; background: var(--gold);
  }

  .details { position: absolute; left: 269px; top: 60px; color: var(--ink); }
  .details__name { font-size: 21px; font-weight: 600; color: var(--gold); line-height: 1.2; }
  .details__role { font-size: 15.5px; line-height: 1.3; }
  .contact { list-style: none; margin-top: 14px; font-size: 14.5px; color: var(--muted); line-height: 20.5px; }
  .contact__label { color: var(--gold); margin-right: 3px; }
  .offers__title { margin-top: 12px; font-size: 18px; color: var(--gold); line-height: 1.2; }
  .offers__list { font-size: 15px; font-style: italic; line-height: 19px; }
  .bullet { color: var(--gold); font-style: normal; font-size: 11px; margin: 0 4px; vertical-align: 1px; }

  .back-mark {
    position: absolute; left: 0; right: 0; top: 88px;
    text-align: center; font-size: 48px; font-weight: 700; line-height: 1;
    color: var(--gold); text-transform: uppercase; letter-spacing: 2px;
  }
  .back-mark span { display: block; }
  .back-offers {
    position: absolute; left: 0; right: 0; top: 253px;
    text-align: center; font-size: 15.5px; color: var(--gold);
  }
  .back-offers strong { font-weight: 700; }
</style>
</head>
<body>
<main class="stage">
  <section class="card card--front" aria-label="Card front">
    <div class="monogram">
      <span class="monogram__dot"></span>
      <span class="monogram__text">RC</span>
    </div>
    <div class="wordmark">Ridgeport<br>Court</div>
    <div class="divider"></div>
    <div class="details">
      <p class="details__name">Marcus Thorne</p>
      <p class="details__role">Boys &amp; Girls Basketball Coach</p>
      <ul class="contact">
        <li><span class="contact__label">p :</span>555-314-7720</li>
        <li><span class="contact__label">e :</span>ridgeport.court@mailzone.example</li>
        <li><span class="contact__label">w :</span>www.ridgeportcourt.net</li>
      </ul>
      <p class="offers__title">Offers:</p>
      <p class="offers__list">Travel Club Program<span class="bullet">●</span>Camps</p>
      <p class="offers__list">Clinics<span class="bullet">●</span>Private Training</p>
    </div>
  </section>

  <section class="card card--back" aria-label="Card back">
    <div class="back-mark"><span>Ridgeport</span><span>Court</span></div>
    <p class="back-offers"><strong>Offers:</strong> Travel Club Program - Camps - Clinics - Private Training</p>
  </section>
</main>
</body>
</html>
```